Real Estate "For Sale" Sign for construction company

We need a sign that we can use to hang on a post and place on the road when we sell a property. The sign will be simple and will need to mainly feature our logo (files attached), as well as the words "For Sale", and then our phone number "(555) 617 3489". The sign will hang on a post that'll look something like the attached picture.

Target Market(s)

Home buyers

Industry/Entity Type

Real Estate

Font styles to use
Serif
Sans Serif

Colors
0054AA
0677BA
7BADD7
CADEEF
E8F1F8
0094D4
00A9DD
6FCCEA
C7EBF8
E9F6FB

Requirements
Must have
• For Sale & our phone number

```html
<!DOCTYPE html>
<html lang="en">
<head>
<meta charset="utf-8">
<title>For Sale Sign</title>
<link rel="stylesheet" href="https://fonts.googleapis.com/css2?family=Bebas+Neue&family=Montserrat:wght@500;700&display=swap">
<style>
  :root {
    --navy: #141f4d;
    --band-top: #243a7c;
    --band-bottom: #1a7cc2;
    --rule-mid: #0094d4;
    --white: #ffffff;
    --backdrop: #eef2f6;
  }
  * { margin: 0; padding: 0; box-sizing: border-box; }
  html, body {
    width: 1200px;
    height: 1002px;
    overflow: hidden;
    background: var(--backdrop);
  }
  .sign {
    position: absolute;
    left: 246px;
    top: 31px;
    width: 708px;
    height: 940px;
    background: var(--white);
    box-shadow: 0 6px 24px rgba(20, 31, 77, 0.15);
    overflow: hidden;
  }
  .sign__headline {
    position: absolute;
    top: 0;
    left: 0;
    width: 100%;
    text-align: center;
    white-space: nowrap;
    font-family: "Bebas Neue", "Oswald", sans-serif;
    font-weight: 400;
    font-size: 246px;
    line-height: 1;
    color: var(--navy);
    transform: scaleX(0.88);
    transform-origin: center;
  }
  .sign__rule {
    position: absolute;
    top: 259px;
    left: 42px;
    width: 618px;
    height: 7px;
    background: linear-gradient(90deg, var(--navy), var(--rule-mid) 55%, var(--navy));
  }
  .sign__contact-label {
    position: absolute;
    top: 318px;
    left: 0;
    width: 100%;
    text-align: center;
    white-space: nowrap;
    font-family: "Montserrat", sans-serif;
    font-weight: 700;
    font-size: 38px;
    line-height: 1;
    letter-spacing: 5px;
    color: var(--navy);
  }
  .sign__phone {
    position: absolute;
    top: 358px;
    left: 0;
    width: 100%;
    text-align: center;
    white-space: nowrap;
    font-family: "Bebas Neue", "Oswald", sans-serif;
    font-weight: 400;
    font-size: 144px;
    line-height: 1;
    color: var(--navy);
    transform: scaleX(0.88);
    transform-origin: center;
  }
  .sign__band {
    position: absolute;
    left: 0;
    bottom: 0;
    width: 100%;
    height: 388px;
    background: linear-gradient(180deg, var(--band-top), var(--band-bottom));
    display: flex;
    align-items: center;
    justify-content: center;
  }
  .sign__brand {
    margin-top: 90px;
    white-space: nowrap;
    font-family: "Montserrat", sans-serif;
    font-weight: 500;
    font-size: 38px;
    color: var(--white);
    text-align: center;
  }
</style>
</head>
<body>
  <main class="sign">
    <h1 class="sign__headline">FOR SALE</h1>
    <div class="sign__rule"></div>
    <p class="sign__contact-label">CONTACT</p>
    <p class="sign__phone">(555).617.3489</p>
    <footer class="sign__band">
      <p class="sign__brand">Ridgeline Valley Properties</p>
    </footer>
  </main>
</body>
</html>
```